Maplerise Trading Inc. needs an innovative idea for letterhead and visiting cards.

Maplerise Trading Inc. is a Canadian brand since 2007. It is a renown dealer of kids and office furniture locally. Moreover, exporting electric fixtures e.g. switches, LED's, down-lights etc. to Middle East and Africa. We have initiated a number of steps including re-branding, to boost our export in 2020. We have successfully designed our new logo a few months ago through 'Artfolio' and now we are looking for an innovative idea for a letterhead.
Some key points:
• Red, black and white are the three colors used in all our packaging and furniture. (grey is optional)
• Shouldn’t be too wide.
• Use of watermark is preferable.
• You can visit our North American site at www.mapleriseinc.com. Export website of the company will be launched soon. www.mapleriseinc.ca
• Same letterhead will be used locally and internationally.
• Our new logo and sample packaging is attached.

```html
<!DOCTYPE html>
<html lang="en">
<head>
<meta charset="utf-8">
<title>Maplerise Trading – Stationery</title>
<link rel="stylesheet" href="https://fonts.googleapis.com/css2?family=Lora:wght@400&family=Archivo:wght@500;700&display=swap">
<style>
  :root{
    --red:#a51115;
    --ink:#1f1f1f;
    --grey:#4a4a4a;
    --paper:#ffffff;
    --stage:#e6e6e6;
    --dark:#1e1e1e;
  }
  *{margin:0;padding:0;box-sizing:border-box}
  html,body{width:1200px;height:1200px;overflow:hidden}
  body{background:var(--stage);position:relative;font-family:"Lora",serif;color:var(--ink)}

  .sheet{position:absolute;background:var(--paper);box-shadow:6px 8px 18px rgba(0,0,0,.35)}

  /* Letterhead */
  .letterhead{left:268px;top:170px;width:667px;height:863px;border-top:5px solid var(--ink)}
  .letterhead::after{content:"";position:absolute;left:0;right:0;bottom:0;height:10px;background:var(--red)}
  .letterhead .brand{position:absolute;left:41px;top:45px;width:300px;height:80px}
  .letterhead .divider{position:absolute;left:403px;top:38px;width:1px;height:76px;background:var(--ink)}
  .letterhead .contact{position:absolute;left:441px;top:35px;font-size:13px;line-height:16.5px;letter-spacing:.4px}

  /* Brand lockup */
  .brand{display:flex;align-items:center;gap:12px}
  .brand-square{width:68px;height:68px;border:3px solid var(--red);border-radius:6px;flex:none}
  .brand-name{font-family:"Archivo",sans-serif;font-weight:500;color:var(--grey);font-size:25px;line-height:1.05;letter-spacing:1.5px;text-transform:uppercase}

  /* Contact list */
  .contact li{list-style:none;display:flex;align-items:center;gap:8px}
  .contact li.plain{padding-left:0}
  .contact svg{width:11px;height:11px;flex:none;fill:none;stroke:var(--red);stroke-width:1.6}
  .contact svg.solid{fill:var(--red);stroke:none}

  /* Card front */
  .card-front{left:92px;top:358px;width:351px;height:200px;border-bottom:4px solid var(--red)}
  .card-front .brand{position:absolute;left:26px;top:84px;gap:7px}
  .card-front .brand-square{width:36px;height:36px;border-width:2px;border-radius:4px}
  .card-front .brand-name{font-size:12.5px;letter-spacing:.8px}
  .card-front .divider{position:absolute;left:176px;top:51px;width:1px;height:96px;background:var(--ink)}
  .card-front .person{position:absolute;left:196px;top:52px}
  .person-name{font-family:"Archivo",sans-serif;font-weight:700;color:var(--red);font-size:13.5px;letter-spacing:.2px}
  .person-role{font-size:8.5px;letter-spacing:.4px;margin-top:1px}
  .card-front .address{font-size:8px;line-height:10px;margin-top:11px;letter-spacing:.2px}
  .card-front .contact{position:static;margin-top:11px;font-size:8.3px;line-height:11px;letter-spacing:.3px}
  .card-front .contact svg{width:7px;height:7px}
  .card-front .contact li{gap:7px}

  /* Card back */
  .card-back{left:781px;top:358px;width:351px;height:200px;background:var(--dark)}
  .card-back .brand{position:absolute;left:74px;top:64px;gap:12px}
  .card-back .brand-square{width:56px;height:56px;background:var(--red);border:none;border-radius:5px}
  .card-back .brand-name{color:#ffffff;font-size:22px;letter-spacing:1.3px}
</style>
</head>
<body>

<section class="sheet letterhead" aria-label="Letterhead">
  <div class="brand">
    <span class="brand-square"></span>
    <span class="brand-name">Maplerise<br>Trading</span>
  </div>
  <span class="divider"></span>
  <ul class="contact">
    <li>58 Cedar Ridge, Suite# B</li>
    <li>1204 Lausanne</li>
    <li><svg class="solid" viewBox="0 0 12 12"><path d="M2.5 1l2 2.3-1 1.3c.7 1.5 1.8 2.6 3.3 3.3l1.3-1L10.5 9l-1 1.8C5.2 10.8 1.2 6.8 1 2.2z"/></svg>000 000 0000</li>
    <li><svg viewBox="0 0 12 12"><rect x="1" y="2.5" width="10" height="7"/><path d="M1 2.5l5 4 5-4"/></svg>info@mapleriseinc.com</li>
    <li><svg viewBox="0 0 12 12"><circle cx="6" cy="6" r="5"/><ellipse cx="6" cy="6" rx="2.2" ry="5"/><path d="M1 6h10M2 3.5h8M2 8.5h8"/></svg>www.mapleriseinc.com</li>
  </ul>
</section>

<section class="sheet card-front" aria-label="Business card front">
  <div class="brand">
    <span class="brand-square"></span>
    <span class="brand-name">Maplerise<br>Trading</span>
  </div>
  <span class="divider"></span>
  <div class="person">
    <p class="person-name">DANIEL ROCHE</p>
    <p class="person-role">Founder &amp; CEO</p>
    <p class="address">58 Cedar Ridge, Suite# B<br>1204 Lausanne</p>
    <ul class="contact">
      <li><svg class="solid" viewBox="0 0 12 12"><path d="M2.5 1l2 2.3-1 1.3c.7 1.5 1.8 2.6 3.3 3.3l1.3-1L10.5 9l-1 1.8C5.2 10.8 1.2 6.8 1 2.2z"/></svg>000 000 0000</li>
      <li><svg viewBox="0 0 12 12"><rect x="1" y="2.5" width="10" height="7"/><path d="M1 2.5l5 4 5-4"/></svg>info@mapleriseinc.com</li>
      <li><svg viewBox="0 0 12 12"><circle cx="6" cy="6" r="5"/><ellipse cx="6" cy="6" rx="2.2" ry="5"/><path d="M1 6h10M2 3.5h8M2 8.5h8"/></svg>www.mapleriseinc.com</li>
    </ul>
  </div>
</section>

<section class="sheet card-back" aria-label="Business card back">
  <div class="brand">
    <span class="brand-square"></span>
    <span class="brand-name">Maplerise<br>Trading</span>
  </div>
</section>

</body>
</html>
```